Venture Capital Investment Firm

We are looking to overhaul our existing website (substantially), with only using the same logos (which we can provide).
We are an investment firm that focuses on making loans to late stage technology companies. Our site should ultimately look like other venture capital firms, and look modern and fresh. We have an existing website www.brenvoltfund.com which this will be replacing, although we will be using a lot of the existing written content, and potentially the numbers of pages we will need, we are not wed to anything else. Please feel free to shoot any questions at any time and thank you in advance for your help!
Websites we like as examples:
https://www.tarnwickbay.com/
https://www.morrowlanefinance.com/
Target Market(s)
Potential investors who will invest in our firm, as well as potentially companies that are looking to borrow money from us.
Coding
Colors
Look and feel

```html
<!DOCTYPE html>
<html lang="en">
<head>
<meta charset="utf-8">
<title>Investor Login — Brenvolt Fund</title>
<link href="https://fonts.googleapis.com/css2?family=Raleway:wght@300;400;500;600&display=swap" rel="stylesheet">
<style>
  :root {
    --navy: #121a4a;
    --ink: #2a3156;
    --field: #f6f7fa;
    --field-line: #4a4f7a;
    --white: #ffffff;
    --sky-top: #3f8aa8;
    --sky-mid: #b3cfdd;
    --sky-low: #ebe4e8;
    --city-warm: #c79a80;
    --city-dark: #3a4450;
    --footer-deep: #0d3a4c;
    --footer-soft: #294c5c;
    --footer-text: #e6eef2;
  }
  * { box-sizing: border-box; margin: 0; padding: 0; }
  html, body { width: 912px; height: 1200px; overflow: hidden; }
  body {
    position: relative;
    font-family: "Raleway", sans-serif;
    background: var(--white);
    color: var(--navy);
  }

  /* Hero */
  .hero {
    position: absolute; left: 0; top: 0; width: 912px; height: 416px;
    background: linear-gradient(160deg, var(--sky-top) 0%, var(--sky-mid) 38%, #dde7ee 62%, var(--sky-low) 100%);
  }
  .hero-skyline {
    position: absolute; left: 0; top: 300px; width: 912px; height: 116px;
    background: linear-gradient(180deg, rgba(230,210,210,0) 0%, var(--city-warm) 35%, #7a6a66 65%, var(--city-dark) 100%);
  }
  .site-nav {
    position: absolute; left: 0; top: 0; width: 912px; height: 64px;
  }
  .brand {
    position: absolute; left: 114px; top: 20px;
    display: flex; align-items: center; gap: 6px;
    font-size: 17px; font-weight: 500; letter-spacing: 0.5px; color: var(--navy);
  }
  .brand-dot { width: 12px; height: 12px; border-radius: 50%; background: var(--navy); }
  .nav-link {
    position: absolute; top: 27px;
    font-size: 8px; font-weight: 400; letter-spacing: 0.4px; color: var(--ink);
  }
  .nav-login {
    position: absolute; left: 689px; top: 16px; width: 109px; height: 32px;
    border: 1px solid var(--navy); border-radius: 16px;
    display: flex; align-items: center; justify-content: center;
    font-size: 8px; letter-spacing: 0.4px; color: var(--ink);
  }
  .hero-title {
    position: absolute; left: 0; top: 163px; width: 912px; text-align: center;
    font-size: 33px; font-weight: 400; color: var(--navy);
  }
  .hero-sub {
    position: absolute; left: 0; top: 209px; width: 912px; text-align: center;
    font-size: 12.5px; font-weight: 300; color: var(--navy);
  }

  /* Login form */
  .form-brand {
    position: absolute; left: 0; top: 480px; width: 912px; text-align: center;
    font-size: 20px; font-weight: 500; color: #4b4d6e; letter-spacing: 0.5px;
  }
  .field-label {
    position: absolute; font-size: 17px; font-weight: 300; color: var(--navy);
  }
  .field-input {
    position: absolute; width: 239px; height: 35px;
    background: var(--field); border: 1px solid var(--field-line); border-radius: 18px;
  }
  .submit-btn {
    position: absolute; left: 405px; top: 712px; width: 102px; height: 34px;
    border: 1px solid var(--navy); border-radius: 17px; background: var(--white);
    display: flex; align-items: center; justify-content: center;
    font-size: 13.5px; font-weight: 500; color: var(--navy);
  }
  .forgot-link {
    position: absolute; left: 0; top: 785px; width: 912px; text-align: center;
    font-size: 11.5px; font-weight: 500; color: var(--navy); text-decoration: underline;
  }

  /* Footer */
  .site-footer {
    position: absolute; left: 0; top: 939px; width: 912px; height: 261px;
    background: linear-gradient(135deg, var(--footer-soft) 0%, var(--footer-deep) 50%, #1f4a5c 100%);
    color: var(--footer-text);
  }
  .footer-brand {
    position: absolute; left: 0; top: 80px; width: 912px;
    display: flex; align-items: center; justify-content: center; gap: 10px;
    font-size: 34px; font-weight: 400; color: var(--white); letter-spacing: 1px;
  }
  .footer-dot { width: 22px; height: 22px; border-radius: 50%; background: var(--white); }
  .footer-link {
    position: absolute; top: 156px; font-size: 8.5px; letter-spacing: 0.4px; color: var(--footer-text);
  }
  .footer-meta {
    position: absolute; left: 0; width: 912px; text-align: center;
    font-size: 5px; color: var(--footer-text);
  }
  .footer-meta u { text-decoration: underline; }
</style>
</head>
<body>

<header class="hero">
  <div class="hero-skyline" role="img" aria-label="Aerial photograph of a city skyline and harbor at sunrise"></div>
  <nav class="site-nav">
    <div class="brand"><span class="brand-dot"></span>Brenvolt Fund</div>
    <span class="nav-link" style="left:303px">STRATEGY</span>
    <span class="nav-link" style="left:388px">ABOUT US</span>
    <span class="nav-link" style="left:473px">TEAM</span>
    <span class="nav-link" style="left:539px">NEWS</span>
    <span class="nav-link" style="left:606px">CONTACT</span>
    <span class="nav-login">INVESTORS LOGIN</span>
  </nav>
  <h1 class="hero-title">Investor Login</h1>
  <p class="hero-sub">Welcome Back</p>
</header>

<main>
  <div class="form-brand">Brenvolt</div>
  <label class="field-label" style="left:276px;top:580px">User Name</label>
  <div class="field-input" style="left:396px;top:573px"></div>
  <label class="field-label" style="left:277px;top:636px">Password</label>
  <div class="field-input" style="left:394px;top:628px"></div>
  <div class="submit-btn">Submit</div>
  <div class="forgot-link">Forgot Password?</div>
</main>

<footer class="site-footer" role="img" aria-label="Photograph of a suspension bridge over a bay at dusk under a dark teal tint">
  <div class="footer-brand"><span class="footer-dot"></span>Brenvolt</div>
  <span class="footer-link" style="left:275px">STRATEGY</span>
  <span class="footer-link" style="left:364px">ABOUT US</span>
  <span class="footer-link" style="left:453px">TEAM</span>
  <span class="footer-link" style="left:523px">NEWS</span>
  <span class="footer-link" style="left:594px">CONTACT</span>
  <p class="footer-meta" style="top:235px">Brenvolt Fund &nbsp;•&nbsp; San Francisco</p>
  <p class="footer-meta" style="top:244px">© 2020 Brenvolt Fund Partners LLC. All Rights Reserved &nbsp;|&nbsp; <u>Legal Disclaimer</u></p>
</footer>

</body>
</html>
```